以前から店舗のすぐ近くを通る幹線道路沿いに看板を出していました。
現在の看板は【3.6mx2.7m】ですが、弊社の看板の下の枠にちょうど空きが出たため上下をつなげて今回【3.6mx5.4m】の大型で製作し直すことになりました。

現在使用中の看板デザインは社内で話し合って作りました。
パソコンや紙で確認していた時は良いと思ったのですが、実際出来上がってみると思ったより文字も小さく遠くからでは内容がわかりづらかったです。
そんな失敗もあり、さらに今回はサイズが2倍になるということもあってプロの方にお願いした方が良いモノが出来上がると思いご依頼させて頂くことになりました。

製作は看板設置会社で行うのでデザインをお願いしたいと思います。

【看板の目的】
当店の認知度拡大と来店促進及びオーダーメイドまくらの販促強化

【設置場所と看板イメージ】
設置場所は車の交通量も多く、看板横のコンビニも車での来店が非常に多い場所です。
(設置場所の画像も添付ファイルに入れています。)
隣に別会社の看板もあるためそれよりも目立つ様にしたいです。
ただ、取り扱っている商品が中~高価格帯のためあまりハデすぎると店舗のイメージには合わないかもしれません。
店舗の「癒し」や「ナチュラル」といったイメージで目立つ看板にしたいという非常に矛盾した要望で恐縮ですが宜しくお願い致します。
看板サイズ:幅3.6mx高さ5.4m【2分割(幅3.6mx高さ2.7mx2枚を上下に設置)】
※看板設置場所の条件で看板本体は上下2分割で設置しないといけません。
※上と下の隙間は10~15cm程の予定です。
※隙間は空きますがデザイン的におかしくなければ一体型の大きなデザインでも
良いかと思っています。

【必ず載せて頂きたい内容】
・店舗ロゴ(添付ファイル有)もしくは店名(寝具の専門店ほしぞの)
・この信号を左折(意味が伝われば表現や言い方は多少変わっても大丈夫です。)
・「オーダーメイドまくら」という文言
(正式には「オーダーメイドまくら」ですが「オーダーまくら」でも可)

【看板設置の目的】
・当店と当店のオーダーメイドまくらの認知度向上と来店促進

【素材について】
・使用できるイメージ画像をいくつか添付ファイルに入れています。
使用した方がいいかどうかも含めてご判断頂ければと思います。
こちらのサービスを初めて利用するのでやり取りが不慣れなところもあるかと思いますが宜しくお願い致します。

今回はこちらのデザインに決定させて頂きました。
伝えたいポイントがわかりやすく表現されているのと、他の看板などと並んだ時にも目立つデザインが社内の選定で選ばれた理由です。
修正にも迅速、丁寧に対応して頂きありがとうございました。

今回は弊社のコンペに多数の方にご参加頂き誠にありがとうございました。
今回初めてクラフタスさんを利用させて頂きましたが、みなさんからすばらしいご提案をたくさん頂き、最後までスタッフみんなで非常に悩みました。
今後も店舗運営上、色々な部分でクラフタスさんを利用させて頂こうと思っていますので今後も宜しくお願い致します。

```html
<!DOCTYPE html>
<html lang="ja">
<head>
<meta charset="utf-8">
<title>オーダーメイドまくら 看板</title>
<link rel="stylesheet" href="https://fonts.googleapis.com/css2?family=M+PLUS+Rounded+1c:wght@900&family=Shippori+Mincho:wght@700&family=Noto+Sans+JP:wght@700;900&display=swap">
<style>
  :root {
    --pink: #e3197f;
    --pink-soft: #f4a6cc;
    --pink-pale: #fbe3ef;
    --white: #ffffff;
    --gap: #eeeeee;
    --mist: #eceef2;
    --cloud: #f7f7f8;
  }
  * { margin: 0; padding: 0; box-sizing: border-box; }
  html, body { width: 812px; height: 1200px; overflow: hidden; background: var(--gap); }
  .sign { position: relative; width: 812px; height: 1200px; }

  /* upper panel */
  .panel-upper { position: absolute; left: 0; top: 0; width: 812px; height: 590px; background: var(--white); overflow: hidden; }
  .photo-area {
    position: absolute; inset: 0;
    background: linear-gradient(180deg, var(--white) 0%, var(--mist) 55%, var(--cloud) 80%, var(--white) 100%);
  }
  .panel-upper .decor { position: absolute; left: 0; top: 0; width: 812px; height: 590px; }
  .catch {
    position: absolute; top: 0; left: 0; width: 812px; height: 590px;
    font-family: "Shippori Mincho", serif; font-weight: 700;
    font-size: 50px; color: var(--pink);
  }
  .catch span {
    position: absolute; writing-mode: vertical-rl;
    line-height: 1; letter-spacing: 10px;
  }
  .catch .c1 { left: 630px; top: 190px; }
  .catch .c2 { left: 560px; top: 255px; }
  .catch .c3 { left: 185px; top: 255px; }
  .catch .c4 { left: 115px; top: 190px; }

  /* lower panel */
  .panel-lower {
    position: absolute; left: 0; top: 612px; width: 812px; height: 588px;
    background: var(--white); border: 14px solid var(--pink); border-bottom: none; overflow: hidden;
  }
  .product {
    position: absolute; left: 0; right: 0; top: 18px; text-align: center;
    font-family: "M PLUS Rounded 1c", sans-serif; font-weight: 900; color: var(--pink);
  }
  .product span { display: block; }
  .product .line1 { font-size: 96px; line-height: 1.1; letter-spacing: -3px; }
  .product .line2 { font-size: 150px; line-height: 1.05; letter-spacing: 10px; }
  .shop {
    position: absolute; left: 246px; top: 318px; display: flex; align-items: center; gap: 20px;
    font-family: "Noto Sans JP", sans-serif; font-weight: 700; color: var(--pink);
  }
  .shop .mark { width: 82px; height: 82px; border: 3px solid var(--pink); }
  .shop .name { font-size: 50px; line-height: 1; }
  .shop .name small { display: block; font-size: 19px; margin-bottom: 8px; }
  .panel-lower .waves { position: absolute; left: 0; bottom: 108px; width: 784px; height: 60px; }
  .direction {
    position: absolute; left: 0; bottom: 0; width: 784px; height: 110px;
    background: var(--pink); display: flex; align-items: center; gap: 30px; padding-left: 28px;
    font-family: "Noto Sans JP", sans-serif; font-weight: 900; color: var(--white);
  }
  .direction .text { font-size: 60px; line-height: 1; letter-spacing: 2px; }
  .direction .text em { font-style: normal; font-size: 80px; }
</style>
</head>
<body>
<div class="sign">
  <section class="panel-upper">
    <div class="photo-area" role="img" aria-label="雲の上で眠る女性と、白いまくらを抱える女性の写真"></div>
    <svg class="decor" viewBox="0 0 812 590" aria-hidden="true">
      <path d="M0 0 H300 C200 40 90 90 0 170 Z" fill="var(--pink-pale)"/>
      <path d="M0 0 H200 C120 30 50 70 0 110 Z" fill="var(--pink)"/>
      <path d="M520 0 H812 V150 C720 70 620 25 520 0 Z" fill="var(--pink-pale)"/>
      <path d="M640 0 H812 V90 C760 45 700 15 640 0 Z" fill="var(--pink)"/>
    </svg>
    <h2 class="catch">
      <span class="c1">眠りが</span><span class="c2">変わると</span>
      <span class="c3">明日が</span><span class="c4">変わる。</span>
    </h2>
  </section>

  <section class="panel-lower">
    <h1 class="product"><span class="line1">オーダーメイド</span><span class="line2">まくら</span></h1>
    <div class="shop">
      <div class="mark"></div>
      <div class="name"><small>寝具の専門店</small>ほしぞの</div>
    </div>
    <svg class="waves" viewBox="0 0 784 60" preserveAspectRatio="none" aria-hidden="true">
      <path d="M0 60 C250 52 500 34 784 0 V60 Z" fill="var(--pink-soft)"/>
      <path d="M0 60 C300 57 550 44 784 22 V60 Z" fill="var(--pink)"/>
    </svg>
    <div class="direction">
      <svg width="110" height="60" viewBox="0 0 110 60" aria-hidden="true">
        <path d="M0 54 L50 6 L50 30 L110 30 L110 54 Z" fill="var(--white)"/>
      </svg>
      <p class="text">この信号を<em>左折</em></p>
    </div>
  </section>
</div>
</body>
</html>
```